School Signage

I am wanting designs for signs completed that prompt students of the school requirements for hats, preparation and play.

I've uploaded rough examples of what we're after, but we would like them stylised and better than the example, including:
- A stylised logo/graphic for the 'Wallumba 1, 2, 3'
- Clear, crisp signage for the words.
- Graphics that reinforce the message of the sign.

We're after three signs:
- One that will be located on the oval to prompt hat use.
- One that will be near the entry prompting the morning routine (please make this one landscape with instructions for 'on time' on one side, and 'late' on the other).
- One that will be located within the school prompting readiness for class.

```html
<!DOCTYPE html>
<html lang="en">
<head>
<meta charset="utf-8">
<title>Ready for Class – Wallumba 1, 2, 3</title>
<link rel="stylesheet" href="https://fonts.googleapis.com/css2?family=Lobster&family=Questrial&display=swap">
<style>
  :root {
    --green: #0b4413;
    --green-text: #0c3d12;
    --yellow: #ffe600;
    --paper: #e7eff9;
    --white: #ffffff;
  }
  * { margin: 0; padding: 0; box-sizing: border-box; }
  html, body { width: 849px; height: 1200px; overflow: hidden; background: var(--paper); }
  .sign {
    position: relative;
    width: 849px;
    height: 1200px;
    background: var(--paper);
    font-family: "Questrial", "Century Gothic", sans-serif;
    color: var(--green-text);
  }
  .linework { position: absolute; inset: 0; }
  .school-name {
    position: absolute;
    left: 620px;
    top: 96px;
    width: 190px;
    display: flex;
    align-items: center;
    gap: 10px;
  }
  .school-name__dot {
    flex: 0 0 40px;
    height: 40px;
    border-radius: 50%;
    background: var(--yellow);
  }
  .school-name__text {
    font-size: 22px;
    line-height: 1.2;
    color: var(--green);
  }
  .hero-art {
    position: absolute;
    left: 73px;
    top: 60px;
    width: 470px;
    height: 375px;
    border-radius: 14px;
    background: radial-gradient(ellipse at 50% 45%, #ffffff 0%, #f4f6f8 50%, #dfe7f0 100%);
  }
  .headline {
    position: absolute;
    left: 150px;
    top: 138px;
    width: 280px;
    text-align: center;
    font-family: "Lobster", cursive;
    font-size: 58px;
    line-height: 68px;
    color: var(--green);
    transform: rotate(-6deg);
    -webkit-text-stroke: 10px var(--yellow);
    paint-order: stroke fill;
  }
  .tagline {
    position: absolute;
    left: 396px;
    top: 421px;
    width: 256px;
    height: 42px;
    border: 3px solid var(--green);
    border-radius: 21px;
    background: var(--yellow);
    font-size: 23px;
    line-height: 36px;
    text-align: center;
    color: var(--green-text);
  }
  .pouch-photo {
    position: absolute;
    left: 152px;
    top: 748px;
    width: 94px;
    height: 60px;
    border-radius: 10px;
    background: linear-gradient(135deg, #b9bcbf 0%, #8b8f92 100%);
    transform: rotate(-18deg);
  }
  .step {
    position: absolute;
    font-size: 42px;
    line-height: 44px;
    color: var(--green-text);
    white-space: nowrap;
  }
  .step--one { left: 318px; top: 560px; }
  .step--two { left: 318px; top: 755px; }
  .step--three { left: 318px; top: 914px; text-align: center; }
  .footer-band {
    position: absolute;
    left: 112px;
    top: 1097px;
    width: 622px;
    height: 103px;
    background: var(--green);
    border-radius: 32px 32px 0 0;
    text-align: center;
  }
  .footer-band__value {
    margin-top: 12px;
    font-size: 44px;
    line-height: 50px;
    color: var(--white);
  }
  .footer-band__label {
    margin-top: 4px;
    font-size: 22px;
    line-height: 26px;
    color: var(--yellow);
  }
</style>
</head>
<body>
<main class="sign">
  <svg class="linework" width="849" height="1200" viewBox="0 0 849 1200" aria-hidden="true">
    <path d="M584 37 H87 A52 52 0 0 0 35 89 V1045 A52 52 0 0 0 87 1097 H112" fill="none" stroke="#0b4413" stroke-width="2.5"/>
    <path d="M809 214 V1045 A52 52 0 0 1 757 1097 H734" fill="none" stroke="#0b4413" stroke-width="2.5"/>
    <line x1="152" y1="584" x2="152" y2="966" stroke="#0b4413" stroke-width="4"/>
    <line x1="246" y1="584" x2="246" y2="966" stroke="#0b4413" stroke-width="4"/>
    <g class="step-hex">
      <polygon points="199,505.5 267.5,545 267.5,623 199,662.5 130.5,623 130.5,545" fill="#0b4413"/>
      <polygon points="199,520 255,552 255,616 199,648 143,616 143,552" fill="#ffe600"/>
    </g>
    <g class="step-hex">
      <polygon points="199,699.5 267.5,739 267.5,817 199,856.5 130.5,817 130.5,739" fill="#0b4413"/>
      <polygon points="199,714 255,746 255,810 199,842 143,810 143,746" fill="#ffe600"/>
    </g>
    <g class="step-hex">
      <polygon points="199,887.5 267.5,927 267.5,1005 199,1044.5 130.5,1005 130.5,927" fill="#0b4413"/>
      <polygon points="199,902 255,934 255,998 199,1030 143,998 143,934" fill="#ffe600"/>
    </g>
    <g class="icon-laptop" fill="none" stroke="#0b4413" stroke-width="2">
      <rect x="167" y="558" width="66" height="42" rx="3"/>
      <rect x="172" y="563" width="56" height="32"/>
      <path d="M160 601 H240 L236 610 H164 Z"/>
      <line x1="176" y1="605" x2="224" y2="605" stroke-dasharray="2 2"/>
    </g>
    <g class="icon-cap" fill="none" stroke="#0b4413" stroke-width="2">
      <path d="M166 978 C166 946 186 934 204 934 C224 934 238 948 238 976 Z"/>
      <path d="M166 978 C158 982 150 988 150 994 C150 999 170 998 186 990 C200 984 220 978 238 976"/>
      <circle cx="204" cy="933" r="3"/>
      <path d="M194 946 H208 V956 L201 962 L194 956 Z"/>
    </g>
  </svg>

  <div class="school-name">
    <span class="school-name__dot"></span>
    <span class="school-name__text">Wallumba<br>State High</span>
  </div>

  <div class="hero-art" role="img" aria-label="Spiral notepad surrounded by a globe, graduation cap, magnifying glass, alarm clock, crayons and a blue backpack"></div>
  <h1 class="headline">Are you ready for class?</h1>

  <p class="tagline">The Wallumba 1, 2, 3</p>

  <div class="pouch-photo" role="img" aria-label="Grey lockable phone pouch with its unlocking base"></div>

  <p class="step step--one">1. Laptop/workbook</p>
  <p class="step step--two">2. Phone in Pocketlock</p>
  <p class="step step--three">3. Correct uniform<br>(including hat)</p>

  <footer class="footer-band">
    <p class="footer-band__value">Curiosity and Drive</p>
    <p class="footer-band__label">Wallumba Learner Values</p>
  </footer>
</main>
</body>
</html>
```